Brightpath Tutors Homepage and Landing Page Redesign

Brightpath Tutors 456 is a premier test preparation, academic consultation, and private tutoring company based in Los Angeles. We offer our tutoring in-person and also online. <br/><br/>We will need three mockups that are as follows:<br/><br/>1. A mockup of a homepage that will be on www.brightpathtutors456.com<br/>2. A mockup of a free-standing true landing page that will be a one-page site where we will direct traffic from a Zindle PPC ad.<br/>3. A mockup of a landing page that will replace a landing page such as the one at www.brightpathtutors456.com/test-prep-services/k-12/sat/ <br/><br/>Please see the word attached for details.

Target Market(s)

Middle School and High School Student Parents, College Students.

Industry/Entity Type

Tutoring

Number of Pages Required

3 page

Colors

Designer to choose colors to be used in the design.

Requirements
Must have
• The design of these 3 pages will need to fit within the overall design of the main website. We're looking for a user-friendly, easy-to-navigate, yet professional design.

```html
<!DOCTYPE html>
<html lang="en">
<head>
<meta charset="utf-8">
<title>Brightpath Tutors — Homepage</title>
<link href="https://fonts.googleapis.com/css2?family=Montserrat:wght@400;500;600;700&family=Open+Sans:wght@400;600;700&display=swap" rel="stylesheet">
<style>
:root{
  --teal:#2b7f7a;
  --teal-dark:#1f6b66;
  --teal-light:#5aa7a1;
  --ink:#2f3a3a;
  --muted:#7b8686;
  --line:#cfd8d7;
  --white:#ffffff;
  --lime:#9cc33b;
  --gold:#f2b51d;
}
*{box-sizing:border-box;margin:0;padding:0}
html,body{width:1200px;height:2916px;overflow:hidden;background:var(--white)}
body{font-family:"Open Sans",Arial,sans-serif;color:var(--ink);position:relative}
h1,h2,h3,.heading{font-family:"Montserrat",Arial,sans-serif}

/* header */
.site-header{height:100px;position:relative}
.brand{position:absolute;left:24px;top:30px;display:flex;align-items:center;gap:10px}
.brand-mark{width:26px;height:26px;border-radius:50%;background:var(--gold)}
.brand-name{font-family:"Montserrat",sans-serif;font-weight:700;font-size:22px;color:var(--teal)}
.top-bar{position:absolute;right:30px;top:12px;display:flex;gap:40px;font-size:13px;color:var(--teal)}
.top-bar span{display:flex;align-items:center;gap:8px}
.main-nav{position:absolute;right:30px;top:58px;display:flex;gap:30px;align-items:center;font-family:"Montserrat",sans-serif;font-size:15px;font-weight:500}
.main-nav a{color:var(--ink);text-decoration:none}
.main-nav a.active{background:var(--teal);color:var(--white);padding:6px 16px}

/* hero */
.hero{position:absolute;top:100px;left:0;width:1200px;height:540px;background:linear-gradient(100deg,#b9c4c2 0%,#8c9a98 40%,#5f6e6c 100%)}
.hero-copy{position:absolute;left:56px;top:86px;width:820px;color:var(--white);font-family:"Montserrat",sans-serif;font-weight:600;font-size:38px;line-height:1.3}
.btn-subscribe{position:absolute;left:56px;top:318px;background:var(--teal);color:var(--white);font-family:"Montserrat",sans-serif;font-weight:600;font-size:19px;padding:14px 40px}
.hero-arrow{position:absolute;right:24px;width:72px;height:60px;background:var(--teal);display:flex;align-items:center;justify-content:center}
.hero-dots{position:absolute;left:520px;top:500px;display:flex;gap:14px}
.hero-dots i{width:26px;height:4px;background:var(--white);display:block}

/* services + form */
.service-card{position:absolute;width:290px;height:280px;background:linear-gradient(160deg,#7f9593,#46605d);display:flex;flex-direction:column;align-items:center;justify-content:flex-end;padding-bottom:26px;color:var(--white);text-align:center}
.service-card svg{margin-bottom:56px}
.service-card h3{font-size:22px;font-weight:600;line-height:1.2;text-transform:uppercase}
.consult-form{position:absolute;left:640px;top:640px;width:540px;height:620px;background:var(--teal-light);padding:30px 40px;color:var(--white)}
.consult-form h2{text-align:center;font-size:31px;font-weight:700;line-height:1.35;margin-bottom:38px}
.field-row{display:flex;gap:40px;margin-bottom:40px}
.field{flex:1;border-bottom:2px solid rgba(255,255,255,.85);padding-bottom:8px;font-size:20px}
.btn-send{display:block;margin:26px auto 0;width:170px;border:2px solid var(--white);text-align:center;padding:8px 0;font-family:"Montserrat",sans-serif;font-size:20px;font-weight:600}

/* results */
.section-title{position:absolute;width:1200px;text-align:center;font-size:24px;font-weight:600;color:var(--teal)}
.search{position:absolute;left:430px;top:1428px;width:300px;border-bottom:2px solid var(--line);font-size:22px;color:#b8c2c1;padding:0 0 8px 4px}
.search svg{position:absolute;right:-36px;top:2px}
.test-tags{position:absolute;left:120px;top:1510px;display:grid;grid-template-columns:repeat(4,86px);gap:28px 26px}
.tag{height:34px;border:2px solid var(--teal);color:var(--teal);font-family:"Montserrat",sans-serif;font-size:13px;font-weight:700;display:flex;align-items:center;justify-content:center}
.tag.active{background:var(--teal);color:var(--white)}
.student{position:absolute;left:680px;top:1510px;display:flex;align-items:center;gap:12px;font-family:"Montserrat",sans-serif;font-weight:700;font-size:17px}
.student-avatar{width:30px;height:30px;border-radius:50%;background:var(--muted)}
.tag-small{position:absolute;left:870px;top:1514px;width:70px;height:26px;background:var(--teal);color:var(--white);font-size:11px;font-weight:700;display:flex;align-items:center;justify-content:center}
.score-label{position:absolute;font-family:"Montserrat",sans-serif;font-size:16px;font-weight:600;color:var(--ink)}
.score-card{position:absolute;width:130px;height:150px;border:2px solid var(--line);text-align:center;padding-top:8px}
.score-card .cap{font-size:17px;color:var(--muted);font-family:"Montserrat",sans-serif;border-bottom:2px solid var(--line);padding-bottom:6px;margin:0 10px}
.score-card .num{font-family:"Montserrat",sans-serif;font-size:52px;font-weight:600;color:var(--teal);line-height:1.2;margin-top:6px}
.score-card .sub{font-size:14px;color:var(--muted)}

/* how it works */
.how-band{position:absolute;top:1940px;left:0;width:1200px;height:340px;background:linear-gradient(90deg,#7fb1ad,#9fc4c1 50%,#6fa39f)}
.how-band .track{position:absolute;left:0;top:0}
.step-label{position:absolute;color:var(--white);font-family:"Montserrat",sans-serif;font-size:14px;font-weight:600;text-align:center;width:200px;line-height:1.25;text-transform:uppercase}

/* tutors */
.tutor{position:absolute;top:2398px;width:150px;text-align:center}
.tutor-photo{width:110px;height:110px;border-radius:50%;margin:0 auto 14px;background:linear-gradient(160deg,#d9dedd,#9ea9a8)}
.tutor h4{font-family:"Montserrat",sans-serif;font-size:14px;font-weight:600}
.tutor p{font-size:13px;color:var(--muted);line-height:1.3;margin-top:4px}
.tutor-arrow{position:absolute;top:2448px;width:44px;height:40px;background:var(--teal);display:flex;align-items:center;justify-content:center}

/* footer */
.site-footer{position:absolute;top:2652px;left:0;width:1200px;height:264px;background:var(--teal-dark);color:var(--white)}
.footer-brand{position:absolute;left:24px;top:88px;background:var(--white);padding:12px 16px;display:flex;align-items:center;gap:8px}
.footer-col{position:absolute;top:22px}
.footer-col h3{font-size:18px;font-weight:600;margin-bottom:14px}
.footer-col li{list-style:none;font-size:13px;line-height:1.55}
.contact-item{display:flex;gap:10px;margin-bottom:10px;font-size:13px;line-height:1.4}
.contact-item b{display:block;font-size:14px}
.subscribe-field{width:120px;height:22px;background:var(--white);margin-top:4px}
.subscribe-send{margin:10px 0 0 60px;width:60px;height:20px;border:1px solid var(--white);font-size:11px;display:flex;align-items:center;justify-content:center}
</style>
</head>
<body>

<header class="site-header">
  <div class="brand"><span class="brand-mark"></span><span class="brand-name">Brightpath Tutors</span></div>
  <div class="top-bar">
    <span><svg width="14" height="14" viewBox="0 0 24 24"><path d="M6.6 10.8a15 15 0 0 0 6.6 6.6l2.2-2.2c.3-.3.7-.4 1-.2 1.1.4 2.3.6 3.6.6.6 0 1 .4 1 1V20c0 .6-.4 1-1 1A17 17 0 0 1 3 4c0-.6.4-1 1-1h3.5c.6 0 1 .4 1 1 0 1.3.2 2.5.6 3.6.1.3 0 .7-.2 1z" fill="#2b7f7a"/></svg>(555) 014-2290</span>
    <span><svg width="16" height="12" viewBox="0 0 16 12"><rect x="0.5" y="0.5" width="15" height="11" fill="none" stroke="#2b7f7a"/><path d="M1 1l7 6 7-6" fill="none" stroke="#2b7f7a"/></svg>contact@brightpathtutors456.com</span>
  </div>
  <nav class="main-nav">
    <a class="active" href="#">Academic Support</a><a href="#">Test Prep</a><a href="#">About</a><a href="#">Resource</a><a href="#">Contact</a>
  </nav>
</header>

<section class="hero" role="img" aria-label="Photo of students studying together in a classroom with a tutor">
  <h1 class="hero-copy">Experienced, professional tutors available for private sessions either in-home in Los Angeles or online, worldwide.</h1>
  <div class="btn-subscribe">Subscribe</div>
  <div class="hero-arrow" style="top:160px"><svg width="26" height="26" viewBox="0 0 26 26"><path d="M4 13h18M14 5l8 8-8 8" fill="none" stroke="#fff" stroke-width="2.5"/></svg></div>
  <div class="hero-arrow" style="top:272px"><svg width="26" height="26" viewBox="0 0 26 26"><path d="M22 13H4M12 5l-8 8 8 8" fill="none" stroke="#fff" stroke-width="2.5"/></svg></div>
  <div class="hero-dots"><i></i><i></i></div>
</section>

<article class="service-card" style="left:20px;top:640px" role="img" aria-label="Academic tutoring, photo of a tutoring session">
  <svg width="80" height="64" viewBox="0 0 80 64" fill="none" stroke="#fff" stroke-width="3"><path d="M4 6h42v26H20l-10 8v-8H4z"/><path d="M34 24h42v26h-6v8l-10-8H34z"/></svg>
  <h3>Academic<br>Tutoring</h3>
</article>
<article class="service-card" style="left:320px;top:640px" role="img" aria-label="K-12 and college test prep, photo of a student writing">
  <svg width="60" height="74" viewBox="0 0 60 74" fill="none" stroke="#fff" stroke-width="3"><rect x="4" y="8" width="52" height="62" rx="4"/><rect x="20" y="3" width="20" height="10"/><path d="M14 30l4 4 7-8M32 31h14M14 50l4 4 7-8M32 51h14"/></svg>
  <h3>K-12 / College<br>Test Prep</h3>
</article>
<article class="service-card" style="left:20px;top:972px" role="img" aria-label="Graduate test prep, photo of a graduate">
  <svg width="84" height="60" viewBox="0 0 84 60" fill="#fff"><path d="M42 4L2 22l40 18 40-18z"/><path d="M18 32v14c0 6 48 6 48 0V32L42 43z"/><rect x="76" y="22" width="3" height="22"/></svg>
  <h3>Graduate<br>Test Prep</h3>
</article>
<article class="service-card" style="left:320px;top:972px" role="img" aria-label="Professional test prep, photo of a professional at work">
  <svg width="76" height="64" viewBox="0 0 76 64" fill="none" stroke="#fff" stroke-width="3"><rect x="4" y="16" width="68" height="44" rx="4"/><path d="M26 16V8h24v8M4 34h68"/><rect x="32" y="30" width="12" height="8" fill="#fff"/></svg>
  <h3>Professional<br>Test Prep</h3>
</article>

<form class="consult-form">
  <h2>Schedule a Free<br>Consultation Today</h2>
  <div class="field-row"><div class="field">First Name</div><div class="field">Last Name</div></div>
  <div class="field-row"><div class="field">Email</div></div>
  <div class="field-row"><div class="field">Phone Number</div></div>
  <div class="field-row"><div class="field">School Name</div><div class="field">Zip Code</div></div>
  <div class="btn-send">Send Email</div>
</form>

<h2 class="section-title" style="top:1318px">Results</h2>
<div class="search">your name
  <svg width="22" height="22" viewBox="0 0 22 22" fill="none" stroke="#2b7f7a" stroke-width="2.5"><circle cx="9" cy="9" r="6"/><path d="M14 14l6 6"/></svg>
</div>
<div class="test-tags">
  <span class="tag active">MCAT</span><span class="tag">SHSAT</span><span class="tag">TOEFL</span><span class="tag">MCAT</span>
  <span class="tag">SSATS</span><span class="tag">MCAT</span><span class="tag">MCAT</span><span class="tag">MCAT</span>
  <span class="tag">MCAT</span><span class="tag">MCAT</span><span class="tag">MCAT</span><span class="tag">PSATS</span>
  <span class="tag">MCAT</span><span class="tag">SATS</span><span class="tag">MCAT</span><span class="tag">MCAT</span>
  <span class="tag">MCAT</span><span class="tag">MCAT</span><span class="tag">MCAT</span>
</div>
<div class="student"><span class="student-avatar"></span>Mr. Alden</div>
<div class="tag-small">ISEE</div>
<div class="score-label" style="left:748px;top:1600px">Before</div>
<div class="score-label" style="left:960px;top:1582px">After</div>
<div class="score-card" style="left:730px;top:1626px"><div class="cap">Results</div><div class="num">510</div><div class="sub">MCAT</div></div>
<div class="score-card" style="left:940px;top:1608px"><div class="cap">Results</div><div class="num">517</div><div class="sub">MCAT</div></div>

<h2 class="section-title" style="top:1862px">How It Works</h2>
<section class="how-band" role="img" aria-label="Photo of a student at a laptop with a timeline of the tutoring process">
  <svg class="track" width="1200" height="340" viewBox="0 0 1200 340" fill="none" stroke="#fff" stroke-width="3">
    <path d="M80 160H1120"/>
    <path d="M80 146l-14 14 14 14 14-14z" fill="#fff"/>
    <path d="M1120 146l-14 14 14 14 14-14z" fill="#fff"/>
    <path d="M290 60v100M655 60v100M990 60v100M170 160v70M470 160v70M815 160v70"/>
    <circle cx="290" cy="70" r="22" fill="#2b7f7a"/><circle cx="655" cy="70" r="22" fill="#2b7f7a"/><circle cx="990" cy="70" r="22" fill="#2b7f7a"/>
    <circle cx="170" cy="232" r="22" fill="#2b7f7a"/><circle cx="470" cy="232" r="22" fill="#2b7f7a"/><circle cx="815" cy="232" r="22" fill="#2b7f7a"/>
    <path d="M282 66l6 6 10-10M647 66l6 6 10-10M982 66l6 6 10-10M162 228l6 6 10-10M462 228l6 6 10-10M807 228l6 6 10-10" stroke-width="2.5"/>
  </svg>
  <div class="step-label" style="left:190px;top:20px">Tutor match</div>
  <div class="step-label" style="left:555px;top:8px">Personalization<br>Technology</div>
  <div class="step-label" style="left:890px;top:8px">Guarantee your<br>child's success</div>
  <div class="step-label" style="left:70px;top:266px">Our tutor</div>
  <div class="step-label" style="left:370px;top:266px">Proprietary<br>Curricula</div>
  <div class="step-label" style="left:715px;top:266px">Building<br>Confidence</div>
</section>

<h2 class="section-title" style="top:2336px">Our tutor</h2>
<div class="tutor-arrow" style="left:222px"><svg width="18" height="18" viewBox="0 0 18 18"><path d="M12 2L5 9l7 7" fill="none" stroke="#fff" stroke-width="2.5"/></svg></div>
<div class="tutor" style="left:325px"><div class="tutor-photo" role="img" aria-label="Portrait of tutor Daniel P."></div><h4>DANIEL P.</h4><p>Specializes in<br>SAT</p></div>
<div class="tutor" style="left:465px"><div class="tutor-photo" role="img" aria-label="Portrait of tutor Nora K."></div><h4>NORA K.</h4><p>Specializes in<br>ISEE</p></div>
<div class="tutor" style="left:605px"><div class="tutor-photo" role="img" aria-label="Portrait of tutor Lena M."></div><h4>LENA M.</h4><p>Specializes in<br>ACT</p></div>
<div class="tutor" style="left:745px"><div class="tutor-photo" role="img" aria-label="Portrait of tutor Clara B."></div><h4>CLARA B.</h4><p>Specializes in<br>GRE</p></div>
<div class="tutor-arrow" style="left:935px"><svg width="18" height="18" viewBox="0 0 18 18"><path d="M6 2l7 7-7 7" fill="none" stroke="#fff" stroke-width="2.5"/></svg></div>

<footer class="site-footer">
  <div class="footer-brand"><span class="brand-mark" style="width:18px;height:18px"></span><span class="brand-name" style="font-size:15px">Brightpath Tutors</span></div>
  <div class="footer-col" style="left:290px">
    <h3>Contact</h3>
    <div class="contact-item"><svg width="12" height="16" viewBox="0 0 12 16"><path d="M6 0a6 6 0 0 0-6 6c0 4 6 10 6 10s6-6 6-10a6 6 0 0 0-6-6z" fill="#fff"/></svg><div><b>Adress</b>1820 Harbor Lane<br>Suite 300<br>Westfield, CA 90001</div></div>
    <div class="contact-item"><svg width="12" height="12" viewBox="0 0 24 24"><path d="M6.6 10.8a15 15 0 0 0 6.6 6.6l2.2-2.2c.3-.3.7-.4 1-.2 1.1.4 2.3.6 3.6.6.6 0 1 .4 1 1V20c0 .6-.4 1-1 1A17 17 0 0 1 3 4c0-.6.4-1 1-1h3.5c.6 0 1 .4 1 1 0 1.3.2 2.5.6 3.6.1.3 0 .7-.2 1z" fill="#fff"/></svg><div><b>Phone</b>(555) 014-2290</div></div>
    <div class="contact-item"><svg width="14" height="10" viewBox="0 0 16 12"><rect x="0.5" y="0.5" width="15" height="11" fill="none" stroke="#fff"/><path d="M1 1l7 6 7-6" fill="none" stroke="#fff"/></svg><div><b>Email</b>contact@brightpathtutors456.com</div></div>
  </div>
  <div class="footer-col" style="left:540px">
    <h3>Popular Services</h3>
    <ul><li>SAT</li><li>SSA</li><li>LSAT</li><li>ISEE</li><li>GRE</li></ul>
  </div>
  <div class="footer-col" style="left:780px">
    <h3>MORE INFO</h3>
    <ul><li>Tutoring Resources</li><li>FAQ</li><li>Blog</li><li>Guaranteed Scholarship</li><li>Free Diagnostic Test</li><li>privacy &amp; terms of use</li></ul>
  </div>
  <div class="footer-col" style="left:1025px">
    <h3>Subscribe</h3>
    <div class="subscribe-field"></div>
    <div class="subscribe-send">Send</div>
  </div>
</footer>

</body>
</html>
```